Civil engineering company | Billboard

We need a billboard design for Velmora- civil engineering company. We want big logo in the center of billboard and web site (www.velmora.hr) below the logo. Also, we want an subtle abstract pattern in the background. Dimensions of the billboard are: width :10 m, height: 2m. Design must be celan and modern.
Industry/Entity Type
Civil engineering
Font styles to use
Sans Serif
Colors
F0912C
F2A743
F7CA91
FBE8D2
FDF5EE
Requirements
Must have
- Logo and new unique pattern design for Velmroa company
Should not have
- pictures of construction machinery and tools

```html
<!DOCTYPE html>
<html lang="hr">
<head>
<meta charset="utf-8">
<title>Velmora – billboard</title>
<link rel="stylesheet" href="https://fonts.googleapis.com/css2?family=Raleway:wght@400;500;700&display=swap">
<style>
  :root {
    --orange: #F0912C;
    --orange-light: #F2A743;
    --peach: #F7CA91;
    --cream: #FBE8D2;
    --paper: #FDF5EE;
    --white: #ffffff;
    --rose: #d9527a;
    --lilac: #d9b3df;
    --ink: #4a4a4a;
    --stage: #252a33;
  }
  html, body {
    margin: 0;
    padding: 0;
    width: 1073px;
    height: 1200px;
    overflow: hidden;
    background: var(--stage);
    font-family: "Raleway", Arial, sans-serif;
  }
  .billboard {
    position: absolute;
    left: 36px;
    top: 500px;
    width: 1000px;
    height: 200px;
    overflow: hidden;
    background: radial-gradient(ellipse at 50% 55%, var(--white) 0%, var(--white) 45%, var(--paper) 100%);
  }
  .pattern {
    position: absolute;
    top: 0;
    width: 320px;
    height: 200px;
  }
  .pattern--left {
    left: 0;
    background: linear-gradient(160deg, var(--orange) 0%, var(--orange-light) 30%, var(--rose) 70%, var(--lilac) 100%);
    -webkit-mask-image: linear-gradient(90deg, #000 0%, #000 35%, transparent 100%);
    mask-image: linear-gradient(90deg, #000 0%, #000 35%, transparent 100%);
  }
  .pattern--right {
    right: 0;
    background: linear-gradient(200deg, var(--orange) 0%, var(--orange-light) 30%, var(--rose) 70%, var(--lilac) 100%);
    -webkit-mask-image: linear-gradient(270deg, #000 0%, #000 35%, transparent 100%);
    mask-image: linear-gradient(270deg, #000 0%, #000 35%, transparent 100%);
  }
  .waves {
    position: absolute;
    top: -20px;
    width: 160px;
    height: 240px;
    background: radial-gradient(ellipse 50% 50% at 50% 50%, rgba(247,202,145,0.45) 0%, rgba(251,232,210,0.25) 55%, rgba(253,245,238,0) 100%);
  }
  .waves--left { left: 260px; }
  .waves--right { right: 260px; }
  .brand {
    position: absolute;
    left: 0;
    right: 0;
    top: 30px;
    text-align: center;
  }
  .brand-mark {
    display: block;
    width: 66px;
    height: 66px;
    margin: 0 auto 8px;
    border: 2px solid var(--ink);
    box-sizing: border-box;
  }
  .brand-name {
    margin: 0;
    font-weight: 500;
    font-size: 30px;
    letter-spacing: 1px;
    line-height: 1;
    color: var(--orange);
  }
  .brand-tagline {
    margin: 3px 0 0;
    font-weight: 700;
    font-size: 8px;
    letter-spacing: 0.2px;
    color: var(--ink);
  }
  .web-band {
    position: absolute;
    left: 345px;
    bottom: 0;
    width: 310px;
    height: 28px;
  }
  .web-band-shape { position: absolute; inset: 0; }
  .web-address {
    position: absolute;
    inset: 0;
    display: flex;
    align-items: center;
    justify-content: center;
    gap: 4px;
    color: var(--white);
    font-size: 19px;
    font-weight: 400;
    letter-spacing: 0.5px;
  }
  .web-address strong { font-weight: 700; }
  .globe { width: 11px; height: 11px; flex: none; }
</style>
</head>
<body>
  <section class="billboard">
    <div class="pattern pattern--left" role="img" aria-label="Abstract low-poly triangle pattern in orange, rose and lilac"></div>
    <div class="pattern pattern--right" role="img" aria-label="Abstract low-poly triangle pattern in orange, rose and lilac"></div>
    <div class="waves waves--left" role="img" aria-label="Faint golden flowing line pattern"></div>
    <div class="waves waves--right" role="img" aria-label="Faint golden flowing line pattern"></div>

    <div class="brand">
      <span class="brand-mark"></span>
      <h1 class="brand-name">VELMORA</h1>
      <p class="brand-tagline">IZVOĐENJE I VOĐENJE GRAĐEVINSKIH RADOVA</p>
    </div>

    <div class="web-band">
      <svg class="web-band-shape" width="310" height="28" viewBox="0 0 310 28" aria-hidden="true">
        <polygon points="10,0 300,0 310,28 0,28" fill="var(--orange)"/>
      </svg>
      <div class="web-address">
        <svg class="globe" viewBox="0 0 12 12" aria-hidden="true">
          <circle cx="6" cy="6" r="5" fill="none" stroke="#fff" stroke-width="1.2"/>
          <line x1="1" y1="6" x2="11" y2="6" stroke="#fff" stroke-width="1"/>
          <ellipse cx="6" cy="6" rx="2.2" ry="5" fill="none" stroke="#fff" stroke-width="1"/>
        </svg>
        <span>www.<strong>velmora</strong>.hr</span>
      </div>
    </div>
  </section>
</body>
</html>
```